Company Employee Onboarding Presentation

We need a custom PowerPoint design for a company presentation. This presentation will be sent to new employees during their onboarding/hiring process. We have attached a current mock-up of the presentation - but this is for content only. We do not like the style of the mock-up. We're a commercial real estate investment company based in Los Angeles, CA. Our website is: www.marnwickhold.com.

One artistic element that we want in the presentation is that we want a timeline similar to the attached file, but want to overlay a rising bar chart from left to right that shows the total number of units owned rising through the years. We would like this to be in the background though by using a low opacity value for the color of the graph. A great example of what we want the timeline to look like is at the bottom of the following webpage (we would just need to add the rising bar chart in the background). https://www.tolvercastlecap.com/firm. This timeline is what would take the place of page 4 of the attached PP presentation.

In addition to our company landing page, the following website is representative of a style we like: https://www.qeo.com

```html
<!DOCTYPE html>
<html lang="en">
<head>
<meta charset="utf-8">
<title>The Marnwick Group – Onboarding Deck</title>
<link href="https://fonts.googleapis.com/css2?family=Montserrat:wght@400;500;600&family=Roboto:wght@400;500&family=Oswald:wght@500&display=swap" rel="stylesheet">
<style>
:root{
  --board:#d8dada;
  --slide:#f2f2f2;
  --red:#c1272d;
  --grey:#b5b5b5;
  --ink:#3a3a3a;
  --col-capital:#e3dddc;
  --col-communities:#b9b9b9;
  --col-impact:#f4d1b2;
}
*{box-sizing:border-box;margin:0;padding:0}
html,body{width:1049px;height:1200px;overflow:hidden;background:var(--board)}
body{position:relative;font-family:'Montserrat',sans-serif;color:var(--ink)}
.slide{position:absolute;width:428px;height:241px;background:var(--slide);overflow:hidden;box-shadow:0 4px 8px rgba(0,0,0,.25)}
.col-a{left:81px}.col-b{left:536px}
.row-1{top:82px}.row-2{top:348px}.row-3{top:618px}.row-4{top:882px}
.title-tab{position:absolute;left:0;top:26px;width:25px;height:16px;background:var(--grey)}
.slide-title{position:absolute;left:34px;top:25px;font-family:'Roboto',sans-serif;font-weight:400;font-size:15px;color:var(--red);letter-spacing:.2px;white-space:nowrap}
.brand{position:absolute;right:13px;top:14px;text-align:center}
.brand-name{font-weight:500;font-size:9.5px;color:#222;white-space:nowrap}
.brand-tag{font-size:2.6px;color:#555;margin-top:1px}
.brand-url{font-size:2.6px;color:var(--red);letter-spacing:1.2px;margin-top:2px}
.photo{position:absolute}
/* cover */
.cover-photo{inset:0;background:linear-gradient(180deg,#b9cfe6 0%,#d8e3ec 30%,#cfd0cc 55%,#8d9a73 80%,#5f6e48 100%)}
.cover-band{position:absolute;left:0;right:0;top:26px;height:45px;background:rgba(140,140,140,.78);text-align:center;color:#fff}
.cover-band .name{font-size:21px;font-weight:500;margin-top:4px}
.cover-band .tag{font-size:6px;margin-top:2px}
.cover-url{position:absolute;right:9px;top:19px;font-size:3px;color:var(--red);letter-spacing:1.6px}
/* who we are */
.intro-box{position:absolute;left:44px;top:47px;width:372px;height:28px;background:var(--grey);font-size:5px;line-height:7px;padding:3px 4px;color:#333}
.team-photo{left:0;top:82px;width:228px;height:159px;background:linear-gradient(160deg,#e9edf0,#c8ccd0 45%,#6b6f78);clip-path:ellipse(118% 100% at 60% 100%)}
.team-arc{position:absolute;left:0;top:80px}
.beliefs{position:absolute;left:243px;top:83px;width:175px;font-size:5px;line-height:6.6px}
.beliefs ul{list-style:none;margin-top:8px}
.beliefs li{position:relative;padding-left:12px;margin-bottom:3.6px}
.beliefs li::before{content:"";position:absolute;left:0;top:2px;width:3px;height:3px;border-radius:50%;background:var(--red)}
/* business lines */
.line-name{position:absolute;top:71px;width:133px;text-align:center;font-size:11.5px;font-weight:500;color:#222;white-space:nowrap}
.line-col{position:absolute;top:92px;width:133px;height:147px;padding:7px 4px;font-size:4.9px;line-height:6.9px;color:#333}
.line-col p+p{margin-top:6px}
.capital{left:14px;background:var(--col-capital)}
.communities{left:149px;background:var(--col-communities)}
.impact{left:285px;background:var(--col-impact)}
/* history */
.history-svg{position:absolute;left:0;top:0}
.units-bar{fill:var(--red);opacity:.09}
.units-label{font-family:'Montserrat',sans-serif;font-size:3.4px;fill:var(--red);opacity:.45}
.note{position:absolute;width:56px;font-size:2.9px;line-height:3.8px;color:#444}
.note b{display:block;color:var(--red);font-weight:600;font-size:3.2px;margin-bottom:1.5px}
/* stats */
.stat{position:absolute;width:76px;height:76px;margin:-38px 0 0 -38px;text-align:center}
.stat-ring{position:absolute;left:0;top:0}
.stat-body{position:absolute;left:0;right:0;top:4px;bottom:-4px;display:flex;flex-direction:column;align-items:center;justify-content:center;font-family:'Roboto',sans-serif;font-size:4.6px;line-height:6px;color:#333}
.stat-num{font-family:'Oswald',sans-serif;font-size:8.5px;color:var(--red);margin-top:3px}
.stat-icon{margin-bottom:3px}
/* map */
.map{left:102px;top:61px;width:298px;height:167px;background:radial-gradient(ellipse at 30% 55%,#c1272d 0 22%,transparent 23%),radial-gradient(ellipse at 72% 45%,#c1272d 0 18%,transparent 19%),#bdbdbd;border-radius:40% 50% 45% 40%/30% 35% 60% 50%}
/* tomorrow */
.goals{position:absolute;left:36px;top:58px;width:250px;list-style:none;font-size:5.1px;line-height:6.9px}
.goals li{position:relative;padding-left:18px;margin-bottom:6px}
.goals li svg{position:absolute;left:0;top:0}
.work-photo{left:290px;top:48px;width:138px;height:193px;background:linear-gradient(200deg,#3a3431,#8a7a6c 45%,#d6c8b8);clip-path:ellipse(100% 100% at 100% 100%)}
.work-arc{position:absolute;left:284px;top:44px}
/* values */
.value{position:absolute;display:flex;align-items:flex-start;gap:9px;font-size:8.4px;line-height:10px;color:#222}
.value svg{flex:none;margin-top:-1px}
</style>
</head>
<body>

<!-- Cover -->
<section class="slide col-a row-1">
  <div class="photo cover-photo" role="img" aria-label="Modern white apartment building with trees and a courtyard walkway under a blue sky"></div>
  <div class="cover-url">www.marnwickhold.com</div>
  <div class="cover-band">
    <div class="name">The Marnwick Group</div>
    <div class="tag">Providing innovative housing solutions nationwide.</div>
  </div>
</section>

<!-- Who we are -->
<section class="slide col-b row-1">
  <div class="brand"><div class="brand-name">The Marnwick Group</div><div class="brand-tag">Providing innovative housing solutions nationwide.</div><div class="brand-url">www.marnwickhold.com</div></div>
  <div class="title-tab"></div>
  <h2 class="slide-title" style="left:44px">WHO WE ARE</h2>
  <div class="intro-box">The Marnwick Group develops and invests nationally in quality real estate projects across multiple business lines. We approach business through an entrepreneurial lens, cultivating a team who acts entrepreneurially and rewards team members commensurate with their contributions. This approach drives us to produce outsized returns.</div>
  <div class="photo team-photo" role="img" aria-label="Group of business colleagues cheering with raised arms in a bright office"></div>
  <svg class="team-arc" width="200" height="60" viewBox="0 0 200 60"><path d="M1 50 Q70 -10 182 30" fill="none" stroke="var(--red)" stroke-width="2"/></svg>
  <div class="beliefs">
    While what we do determines our day-to-day, it's what we believe that makes us The Marnwick Group.
    <ul>
      <li>We believe in being action oriented. Results are achieved by compressing the distance between good ideas and great execution.</li>
      <li>We believe in authenticity. It doesn't take a suit and tie to solve big problems. Work hard and be yourself.</li>
      <li>We believe in big goals. In order to achieve uncommon results, our goals must push us out of our comfort zone, beyond what we think is possible.</li>
      <li>We believe we can do well while doing good. We give back to our communities and aim to have a lasting social impact.</li>
      <li>We believe work and fun are not mutually exclusive. When done right, hard work can be a lot of fun.</li>
      <li>We believe in a thoughtful approach. We utilize our experience and a considered approach to make swift, reasoned and forward-thinking decisions.</li>
    </ul>
  </div>
</section>

<!-- Business lines -->
<section class="slide col-a row-2">
  <div class="brand"><div class="brand-name">The Marnwick Group</div><div class="brand-tag">Providing innovative housing solutions nationwide.</div><div class="brand-url">www.marnwickhold.com</div></div>
  <div class="title-tab"></div>
  <h2 class="slide-title">OUR BUSINESS LINES</h2>
  <div class="line-name" style="left:14px">Marnwick Capital</div>
  <div class="line-name" style="left:149px;font-size:9.5px;top:73px">Marnwick Communities</div>
  <div class="line-name" style="left:285px;font-size:8.5px;top:74px">Marnwick Impact Housing</div>
  <div class="line-col capital">
    <p>Marnwick Capital is The Marnwick Group's market rate investment vehicle founded on the basis of value investing philosophies, focusing on distressed, opportunistic, value-add and niche market real estate assets. Within these classes, Marnwick typically targets underperforming properties that often require significant renovations and hands-on management to realize the assets' full potential.</p>
    <p>Marnwick constantly assesses market conditions and end-user demand in order to identify short- and long-term inefficiencies and arbitrage opportunities. Subsequent to identifying broader market opportunity, Marnwick applies a methodical approach to set the stage for realizing superior returns.</p>
  </div>
  <div class="line-col communities">
    <p>In the context of a deepening affordability crisis, The Marnwick Group entered affordable housing in 2013 with the establishment of Marnwick Communities, a developer, owner, and operator focused on providing affordable housing nationwide.</p>
    <p>Through property-based Section 8 subsidies, Low Income Housing Tax Credits, and additional programs, Marnwick aims to preserve and expand long term housing affordability for low-income households. Marnwick and its principals have a proven track record in the industry for safeguarding and growing the number of affordable units throughout the country.</p>
  </div>
  <div class="line-col impact">
    <p>Marnwick Impact Housing was founded to address the housing problem for middle income earners – moderate-income individuals that cannot afford to reside in the communities in which they work.</p>
    <p>Drawing upon the company's affordable and market-rate housing expertise, Marnwick Impact Housing creates quality, income restricted housing units. The essential housing properties serve middle-income residents who earn incomes in excess of traditional affordable housing restrictions and yet cannot afford market rate housing without becoming rent burdened. The company undertakes these projects through strategic public-private partnerships with government agencies and financial institutions.</p>
  </div>
</section>

<!-- Company history -->
<section class="slide col-b row-2">
  <div class="title-tab"></div>
  <h2 class="slide-title">COMPANY HISTORY</h2>
  <svg class="history-svg" width="428" height="241" viewBox="0 0 428 241">
    <!-- units owned, rising background bars -->
    <g class="units-chart">
      <rect class="units-bar" x="12" y="222" width="30" height="19"/>
      <rect class="units-bar" x="46" y="214" width="30" height="27"/>
      <rect class="units-bar" x="80" y="204" width="30" height="37"/>
      <rect class="units-bar" x="114" y="190" width="30" height="51"/>
      <rect class="units-bar" x="148" y="176" width="30" height="65"/>
      <rect class="units-bar" x="182" y="160" width="30" height="81"/>
      <rect class="units-bar" x="216" y="142" width="30" height="99"/>
      <rect class="units-bar" x="250" y="124" width="30" height="117"/>
      <rect class="units-bar" x="284" y="104" width="30" height="137"/>
      <rect class="units-bar" x="318" y="84" width="30" height="157"/>
      <rect class="units-bar" x="352" y="62" width="30" height="179"/>
      <rect class="units-bar" x="386" y="40" width="30" height="201"/>
      <text class="units-label" x="414" y="37" text-anchor="end">Total units owned: 7,500+</text>
    </g>
    <g fill="none" stroke="var(--red)" stroke-width=".8">
      <path d="M16 160 V230 M76 160 V230 M129 160 V230 M147 144 V72 M203 145 V26 M278 117 V20 M352 98 V20"/>
    </g>
    <g fill="var(--red)" font-family="Montserrat,sans-serif" font-size="5" font-weight="600">
      <g><path d="M16 160 h34 l5 4 -5 4 h-34z"/><text x="20" y="166" fill="#fff">2010</text></g>
      <g><path d="M76 160 h34 l5 4 -5 4 h-34z"/><text x="80" y="166" fill="#fff">2011</text></g>
      <g><path d="M129 160 h18 l5 4 -5 4 h-18z"/><text x="131" y="166" fill="#fff">2012</text></g>
      <g><path d="M147 144 h24 l5 4 -5 4 h-24z"/><text x="149" y="150" fill="#fff">2013</text></g>
      <g><path d="M203 145 h22 l5 4 -5 4 h-22z"/><text x="205" y="151" fill="#fff">2015</text></g>
      <g><path d="M222 132 h22 l5 4 -5 4 h-22z"/><text x="224" y="138" fill="#fff">2016</text></g>
      <g><path d="M240 119 h22 l5 4 -5 4 h-22z"/><text x="242" y="125" fill="#fff">2017</text></g>
      <g><path d="M278 117 h22 l5 4 -5 4 h-22z"/><text x="280" y="123" fill="#fff">2019</text></g>
      <g><path d="M298 108 h22 l5 4 -5 4 h-22z"/><text x="300" y="114" fill="#fff">2020</text></g>
      <g><path d="M318 98 h22 l5 4 -5 4 h-22z"/><text x="320" y="104" fill="#fff">2021</text></g>
      <g><path d="M352 98 h22 l5 4 -5 4 h-22z"/><text x="354" y="104" fill="#fff">2021</text></g>
      <g><path d="M358 76 h22 l5 4 -5 4 h-22z"/><text x="360" y="82" fill="#fff">2022</text></g>
    </g>
  </svg>
  <div class="note" style="left:18px;top:100px"><b>A bold start in a tough market</b>In 2010 we founded the company during the downturn, seeking value in overlooked multifamily assets. We began small and built a record one deal at a time.</div>
  <div class="note" style="left:18px;top:176px"><b>Start with what you know</b>We focused on neighborhoods we understood, improving tired properties and adding value through careful renovation.</div>
  <div class="note" style="left:78px;top:96px"><b>A first fund takes shape</b>Backed by early partners, we raised our first fund and moved quickly on distressed opportunities.</div>
  <div class="note" style="left:131px;top:176px"><b>Momentum builds</b>After months of patience, a key acquisition closed and later sold at a strong premium.</div>
  <div class="note" style="left:149px;top:76px;width:50px"><b>Doing well while doing good</b>We entered affordable housing, forming our communities platform to preserve quality homes.</div>
  <div class="note" style="left:206px;top:26px;width:68px"><b>A new neighborhood</b>We took on a major redevelopment downtown, using tax credits to renew hundreds of homes and support a growing area.</div>
  <div class="note" style="left:205px;top:160px"><b>Team spirit</b>Friendly competition became a company tradition, bringing our people together.</div>
  <div class="note" style="left:281px;top:22px;width:66px"><b>Solving for the missing middle</b>We launched our impact housing platform to serve teachers, nurses and other essential workers priced out of the cities they serve.</div>
  <div class="note" style="left:280px;top:130px;width:62px"><b>A healthy challenge</b>Our team took on a shared wellness challenge, building habits of focus and persistence.</div>
  <div class="note" style="left:355px;top:22px;width:62px"><b>Room to grow</b>We moved to a new headquarters built around collaboration, with space to celebrate wins.</div>
  <div class="note" style="left:354px;top:112px;width:62px"><b>Moving on up</b>Our growth is the result of a dedicated team that keeps delivering exceptional results.</div>
</section>

<!-- Where are we now -->
<section class="slide col-a row-3">
  <div class="brand"><div class="brand-name">The Marnwick Group</div><div class="brand-tag">Providing innovative housing solutions nationwide.</div><div class="brand-url">www.marnwickhold.com</div></div>
  <div class="title-tab"></div>
  <h2 class="slide-title">WHERE ARE WE NOW</h2>
  <div class="stat" style="left:97px;top:101px">
    <svg class="stat-ring" width="76" height="76" viewBox="0 0 76 76"><path d="M4 28 A36 36 0 0 1 72 28" fill="none" stroke="var(--red)" stroke-width="1"/><circle cx="38" cy="40" r="32" fill="none" stroke="var(--grey)" stroke-width="3"/></svg>
    <div class="stat-body"><svg class="stat-icon" width="18" height="12"><rect x="1" y="4" width="5" height="8" fill="var(--red)"/><rect x="7" y="1" width="5" height="11" fill="var(--red)"/><rect x="13" y="3" width="4" height="9" fill="var(--red)"/></svg>Apartment Units<br>Acquired<span class="stat-num">7,500 +</span></div>
  </div>
  <div class="stat" style="left:205px;top:101px">
    <svg class="stat-ring" width="76" height="76" viewBox="0 0 76 76"><path d="M4 28 A36 36 0 0 1 72 28" fill="none" stroke="var(--red)" stroke-width="1"/><circle cx="38" cy="40" r="32" fill="none" stroke="var(--grey)" stroke-width="3"/></svg>
    <div class="stat-body"><svg class="stat-icon" width="20" height="9"><circle cx="5" cy="3" r="2" fill="var(--red)"/><circle cx="10" cy="2.5" r="2" fill="var(--red)"/><circle cx="15" cy="3" r="2" fill="var(--red)"/><rect x="1" y="6" width="18" height="3" rx="1.5" fill="var(--red)"/></svg>Senior<br>Management Team<br>Acquisition Experience<span class="stat-num">Over $4 billion</span></div>
  </div>
  <div class="stat" style="left:313px;top:101px">
    <svg class="stat-ring" width="76" height="76" viewBox="0 0 76 76"><path d="M4 28 A36 36 0 0 1 72 28" fill="none" stroke="var(--red)" stroke-width="1"/><circle cx="38" cy="40" r="32" fill="none" stroke="var(--grey)" stroke-width="3"/></svg>
    <div class="stat-body"><svg class="stat-icon" width="12" height="14"><rect x="1" y="1" width="10" height="12" fill="none" stroke="#555" stroke-width=".8"/><path d="M3 5h6M3 7h6M3 9h4" stroke="var(--red)" stroke-width=".8"/></svg>Current Assets<br>Under Management<span class="stat-num">$1+ billion</span></div>
  </div>
  <div class="stat" style="left:151px;top:177px">
    <svg class="stat-ring" width="76" height="76" viewBox="0 0 76 76"><path d="M4 28 A36 36 0 0 1 72 28" fill="none" stroke="var(--red)" stroke-width="1"/><circle cx="38" cy="40" r="32" fill="none" stroke="var(--grey)" stroke-width="3"/></svg>
    <div class="stat-body"><svg class="stat-icon" width="20" height="11"><g fill="var(--red)"><rect x="2" y="2" width="3" height="9"/><rect x="7" y="2" width="3" height="9"/><rect x="12" y="2" width="3" height="9"/><rect x="17" y="2" width="2" height="9"/></g></svg>Number of Residents<br>Served<span class="stat-num">13,000+</span></div>
  </div>
  <div class="stat" style="left:259px;top:177px">
    <svg class="stat-ring" width="76" height="76" viewBox="0 0 76 76"><path d="M4 28 A36 36 0 0 1 72 28" fill="none" stroke="var(--red)" stroke-width="1"/><circle cx="38" cy="40" r="32" fill="none" stroke="var(--grey)" stroke-width="3"/></svg>
    <div class="stat-body"><svg class="stat-icon" width="14" height="12"><path d="M3 6 A4 4 0 0 1 11 6Z" fill="var(--red)"/><rect x="2" y="8" width="10" height="4" fill="var(--red)"/></svg>Renovations<br>Performed<span class="stat-num">$60mm+</span></div>
  </div>
  <div class="stat" style="left:367px;top:177px">
    <svg class="stat-ring" width="76" height="76" viewBox="0 0 76 76"><path d="M4 28 A36 36 0 0 1 72 28" fill="none" stroke="var(--red)" stroke-width="1"/><circle cx="38" cy="40" r="32" fill="none" stroke="var(--grey)" stroke-width="3"/></svg>
    <div class="stat-body"><svg class="stat-icon" width="14" height="12"><path d="M1 1V11H13" fill="none" stroke="#555" stroke-width=".8"/><path d="M3 9 6 6 8 7 12 3" fill="none" stroke="var(--red)" stroke-width=".8"/></svg>IRR of Realized<br>Investments –<br>Marnwick Communities<span class="stat-num">34.87%</span></div>
  </div>
</section>

<!-- Portfolio -->
<section class="slide col-b row-3">
  <div class="brand"><div class="brand-name">The Marnwick Group</div><div class="brand-tag">Providing innovative housing solutions nationwide.</div><div class="brand-url">www.marnwickhold.com</div></div>
  <div class="title-tab"></div>
  <h2 class="slide-title">OUR NATIONWIDE PORTFOLIO</h2>
  <div class="photo map" role="img" aria-label="Map of the United States with portfolio states highlighted in red and other states in grey"></div>
</section>

<!-- Tomorrow -->
<section class="slide col-a row-4">
  <div class="brand"><div class="brand-name">The Marnwick Group</div><div class="brand-tag">Providing innovative housing solutions nationwide.</div><div class="brand-url">www.marnwickhold.com</div></div>
  <div class="title-tab"></div>
  <h2 class="slide-title">WHAT DOES TOMORROW LOOK LIKE?</h2>
  <ul class="goals">
    <li><svg width="12" height="10"><path d="M1 5 4 8 11 1" fill="none" stroke="var(--red)" stroke-width="1"/></svg>We will be a market leader. We will pursue growth and innovation to achieve industry beating returns and exponentially expand our portfolio through new and existing business lines.</li>
    <li><svg width="12" height="10"><path d="M1 5 4 8 11 1" fill="none" stroke="var(--red)" stroke-width="1"/></svg>We will positively impact those we touch. We have a responsibility to create opportunity for our residents and our employees. Investing in the success of both parties, particularly by empowering individuals, will help us enact the social impact that is sorely needed.</li>
    <li><svg width="12" height="10"><path d="M1 5 4 8 11 1" fill="none" stroke="var(--red)" stroke-width="1"/></svg>We will have a positive impact on those we touch. We will positively impact all stakeholders in our business (residents, employees, communities and investors) by adhering to a high standards in terms of both our fiduciary and social obligations.</li>
    <li><svg width="12" height="10"><path d="M1 5 4 8 11 1" fill="none" stroke="var(--red)" stroke-width="1"/></svg>We will have a positive and lasting effect on residents/communities/etc by doing what's right not what's easy</li>
    <li><svg width="12" height="10"><path d="M1 5 4 8 11 1" fill="none" stroke="var(--red)" stroke-width="1"/></svg>We will reduce our footprint. We recognize that the construction industry has a significant carbon footprint. Through our perpetual desire to innovate through reimagining, reorganizing and reworking, we will find further solutions to substantially reduce the carbon footprint of our communities.</li>
    <li><svg width="12" height="10"><path d="M1 5 4 8 11 1" fill="none" stroke="var(--red)" stroke-width="1"/></svg>We will utilize our expertise to its fullest. The multifamily industry has been one of the highest performing asset classes, and is poised to remain such. We will outperform the already favorable market by applying all of our experience to mitigate risk and enhance upside.</li>
  </ul>
  <div class="photo work-photo" role="img" aria-label="Two colleagues working together at a laptop"></div>
  <svg class="work-arc" width="144" height="197" viewBox="0 0 144 197"><path d="M2 196 A150 150 0 0 1 144 2" fill="none" stroke="var(--red)" stroke-width="2"/></svg>
</section>

<!-- Core values -->
<section class="slide col-b row-4">
  <div class="brand"><div class="brand-name">The Marnwick Group</div><div class="brand-tag">Providing innovative housing solutions nationwide.</div><div class="brand-url">www.marnwickhold.com</div></div>
  <div class="title-tab"></div>
  <h2 class="slide-title">OUR CORE VALUES</h2>
  <div class="value" style="left:37px;top:74px"><svg width="14" height="12"><path d="M7 12V2M3 6 7 2 11 6" fill="none" stroke="var(--red)" stroke-width="1.2"/></svg>We do what's right, not what's easy</div>
  <div class="value" style="left:37px;top:95px"><svg width="14" height="12"><circle cx="5" cy="3" r="2" fill="var(--red)"/><path d="M2 11 5 6 9 9 13 8" fill="none" stroke="var(--red)" stroke-width="1.2"/></svg>We lead by example</div>
  <div class="value" style="left:37px;top:116px"><svg width="14" height="12"><rect x="1" y="1" width="12" height="10" rx="2" fill="none" stroke="var(--red)" stroke-width="1"/></svg>We harness the collective and<br>collaborative power or the team</div>
  <div class="value" style="left:37px;top:150px"><svg width="14" height="12"><path d="M1 6 7 1 13 6V11H1Z" fill="none" stroke="var(--red)" stroke-width="1"/></svg>We empower individuals</div>
  <div class="value" style="left:37px;top:171px"><svg width="14" height="12"><circle cx="7" cy="6" r="5" fill="none" stroke="var(--red)" stroke-width="1"/><circle cx="7" cy="6" r="1.5" fill="var(--red)"/></svg>We make swift, reasoned and<br>forward-thinking decisions</div>
  <div class="value" style="left:37px;top:202px"><svg width="14" height="12"><rect x="1" y="2" width="12" height="9" fill="none" stroke="var(--red)" stroke-width="1"/><path d="M7 2V11" stroke="var(--red)" stroke-width="1"/></svg>We pursue lifelong learning</div>
  <div class="value" style="left:235px;top:74px"><svg width="14" height="12"><rect x="3" y="1" width="8" height="10" rx="1" fill="none" stroke="var(--red)" stroke-width="1"/><path d="M5 6 7 8 9 4" fill="none" stroke="var(--red)" stroke-width="1"/></svg>We reward results</div>
  <div class="value" style="left:235px;top:95px"><svg width="14" height="12"><circle cx="7" cy="6" r="4" fill="none" stroke="var(--red)" stroke-width="1"/><path d="M7 0V12M1 6H13" stroke="var(--red)" stroke-width=".8"/></svg>We approach each day with intention</div>
  <div class="value" style="left:235px;top:116px"><svg width="14" height="12"><circle cx="7" cy="5" r="4" fill="none" stroke="var(--red)" stroke-width="1"/><path d="M5 10H9" stroke="var(--red)" stroke-width="1.2"/></svg>We innovate through reimagining,<br>reorganizing and reworking</div>
  <div class="value" style="left:235px;top:150px"><svg width="14" height="12"><circle cx="7" cy="2.5" r="2" fill="var(--red)"/><path d="M7 5V9M4 12 7 9 10 12M3 7H11" fill="none" stroke="var(--red)" stroke-width="1"/></svg>We think and act like owners</div>
  <div class="value" style="left:235px;top:171px"><svg width="14" height="12"><circle cx="7" cy="2.5" r="2" fill="none" stroke="var(--red)" stroke-width="1"/><path d="M7 5V9M4 12 7 9 10 12M2 4 7 6 12 4" fill="none" stroke="var(--red)" stroke-width="1"/></svg>We work hard and have fun</div>
</section>

</body>
</html>
```